Etiketten-Design für Glühwein/Kinderpunsch
Zielgruppe
wir sind ein konventioneller Landwirtschaftlicher Betrieb. Ein Standbein sind unsere 2ha große Heidelbeerplantage. wir haben eine 'beerige Produktpalette' und brauchen für die Saisonware Glühwein/Kinderpunsch neue Etiketten; Zielgruppe: Regionale Vermarkung, Direktvermakrtung, von 0-99,
Aufgabenstellung
peppiges, auffälliges Etiektt, das Lust auf Glühwein/Winter macht und für den alkoholfreie Fruchtpunsch was das Kinder und Erwachsene anspricht
Flaschenetiektt mit den gesetzlichen Vorgaben,
Farben: Unser Logo ist in Lila, hellgrün, dunkelgrün, schwarz und weiß gehalten, sind aber prinzipiell offen für alles

```html
<!DOCTYPE html>
<html lang="de">
<head>
<meta charset="utf-8">
<title>Etiketten Glühwein und Fruchtpunsch</title>
<link rel="stylesheet" href="https://fonts.googleapis.com/css2?family=Jost:wght@600;700;800&display=swap">
<style>
  :root {
    --canvas: #ffffff;
    --violet-deep: #3a0f9a;
    --violet-mid: #5a22c8;
    --violet-band: #1a0a45;
    --violet-type: #a77ce0;
    --blue-deep: #0a2a8a;
    --blue-mid: #1d4fd0;
    --blue-band: #0b1a35;
    --blue-type: #95b2f0;
    --lime: #7ed321;
    --white: #ffffff;
    --photo-dark: #1d1d1b;
  }
  * { box-sizing: border-box; margin: 0; padding: 0; }
  html, body { width: 780px; height: 1200px; overflow: hidden; background: var(--canvas); }
  body { position: relative; font-family: "Jost", "Futura", sans-serif; }

  .label {
    position: absolute;
    top: 337px;
    width: 290px;
    height: 525px;
    overflow: hidden;
  }
  .label--gluehwein { left: 60px; }
  .label--punsch { left: 430px; }

  .label__art { position: absolute; inset: 0; width: 290px; height: 525px; display: block; }

  .brand {
    position: absolute;
    top: 262px;
    left: 0;
    width: 100%;
    display: flex;
    justify-content: center;
    align-items: center;
    gap: 6px;
    color: var(--white);
    font-weight: 700;
    font-size: 15px;
    letter-spacing: 0.3px;
  }
  .brand__dot {
    width: 10px; height: 10px; border-radius: 50%;
    background: var(--white);
  }

  .product-name {
    position: absolute;
    top: 318px;
    left: 0;
    width: 100%;
    text-align: center;
    font-weight: 800;
    font-size: 39px;
    line-height: 47px;
    letter-spacing: -0.5px;
    text-transform: uppercase;
  }
  .label--gluehwein .product-name { color: var(--violet-type); }
  .label--punsch .product-name { color: var(--blue-type); font-size: 42px; line-height: 48px; left: 2px; }

  .badge {
    position: absolute;
    top: 418px;
    left: 74px;
    width: 144px;
    height: 30px;
    background: var(--lime);
    color: var(--white);
    font-weight: 700;
    font-size: 16px;
    line-height: 30px;
    text-align: center;
    letter-spacing: 0.2px;
  }
</style>
</head>
<body>

  <section class="label label--gluehwein">
    <svg class="label__art" viewBox="0 0 290 525">
      <defs>
        <linearGradient id="violet-body" x1="0" y1="0" x2="1" y2="1">
          <stop offset="0" stop-color="#4a16b8"/>
          <stop offset="0.55" stop-color="#3a0f9a"/>
          <stop offset="1" stop-color="#5a22c8"/>
        </linearGradient>
        <linearGradient id="berry-photo" x1="0" y1="0" x2="1" y2="0">
          <stop offset="0" stop-color="#5f9a3a"/>
          <stop offset="0.45" stop-color="#3f55a8"/>
          <stop offset="0.8" stop-color="#6a3a9a"/>
          <stop offset="1" stop-color="#b04a7a"/>
        </linearGradient>
      </defs>
      <rect width="290" height="472" fill="url(#violet-body)" role="img" aria-label="Schneeflocken-Muster auf Lila"/>
      <rect y="472" width="290" height="53" fill="var(--violet-band)"/>
      <polygon points="0,0 290,0 290,166 145,211 0,166" fill="var(--photo-dark)"/>
      <polygon points="0,0 290,0 290,166 145,211 0,166" fill="url(#berry-photo)" opacity="0.9" role="img" aria-label="Foto: Heidelbeeren mit Blättern und ein Glas Glühwein"/>
    </svg>
    <div class="brand"><span class="brand__dot"></span>Brommers Beerenhof</div>
    <h1 class="product-name">Heidelbeer<br>Glühwein</h1>
  </section>

  <section class="label label--punsch">
    <svg class="label__art" viewBox="0 0 290 525">
      <defs>
        <linearGradient id="blue-body" x1="0" y1="0" x2="1" y2="1">
          <stop offset="0" stop-color="#1d4fd0"/>
          <stop offset="0.5" stop-color="#0a2a8a"/>
          <stop offset="1" stop-color="#1a5ae0"/>
        </linearGradient>
        <linearGradient id="fruit-photo" x1="0" y1="0" x2="1" y2="0">
          <stop offset="0" stop-color="#b8283a"/>
          <stop offset="0.35" stop-color="#c84a2a"/>
          <stop offset="0.6" stop-color="#f2a31a"/>
          <stop offset="1" stop-color="#9a5a3a"/>
        </linearGradient>
      </defs>
      <rect width="290" height="472" fill="url(#blue-body)" role="img" aria-label="Schneeflocken-Muster auf Blau"/>
      <rect y="472" width="290" height="53" fill="var(--blue-band)"/>
      <polygon points="0,0 290,0 290,166 145,211 0,166" fill="var(--photo-dark)"/>
      <polygon points="0,0 290,0 290,166 145,211 0,166" fill="url(#fruit-photo)" opacity="0.9" role="img" aria-label="Foto: Glas Fruchtpunsch, halbe Orange und Zimtstangen"/>
    </svg>
    <div class="brand"><span class="brand__dot"></span>Brommers Beerenhof</div>
    <h1 class="product-name">Frucht<br>Punsch</h1>
    <div class="badge">ALKOHOLFREI</div>
  </section>

</body>
</html>
```